Business logo, card, letter head design needed

we run makeup & hair academy, also we have a retail shop in Prahran Vic. we ahve logo for our shop which (glinted tavu Cosmetics) but no logo yet for our academy, we hope can do a double side business card, front for the academy / back for the shop which we would like to use black back ground with our white round logo
Target Market(s)
16 - 40 female
Industry/Entity Type
Retail
Contact Information for Business Card
Larkfield Makeup & Hair Academy (LMHA)
Glinted Tavu Cosmetics
Dorotea Brankelis
Director
47 Tamsworth St. Kelverton Vic 3279
E: dorotea@glowstudiocollege.com.au
M: 61-438217506
Academy web: www.glowstudiocollege.com.au
Shop web: www.glintedtavu.com
Logo Text
Larkfield Makeup & Hair Academy
Logo styles of interest
Wordmark Logo
Lettermark Logo
Look and feel

```html
<!DOCTYPE html>
<html lang="en">
<head>
<meta charset="utf-8">
<title>Glinted Tavu Cosmetics / Larkfield Makeup &amp; Hair Academy – Business Card</title>
<link rel="stylesheet" href="https://fonts.googleapis.com/css2?family=Arimo:wght@400;700&family=Josefin+Sans:wght@300;400&display=swap">
<style>
  :root {
    --stage: #2b2b2b;
    --card-light: #ffffff;
    --card-dark: #050505;
    --ink-dark: #111111;
    --ink-soft: #333333;
    --ink-light: #ffffff;
  }
  * { margin: 0; padding: 0; box-sizing: border-box; }
  html, body {
    width: 1200px;
    height: 900px;
    overflow: hidden;
    background: var(--stage);
  }
  .canvas {
    position: relative;
    width: 1200px;
    height: 900px;
  }
  .card {
    position: absolute;
    left: 330px;
    width: 540px;
    height: 310px;
    box-shadow: 0 10px 30px rgba(0,0,0,0.45);
  }

  /* Shop side */
  .card--shop {
    top: 110px;
    background: var(--card-light);
    color: var(--ink-dark);
    font-family: "Arimo", Arial, sans-serif;
  }
  .shop-name {
    position: absolute;
    left: 40px;
    top: 118px;
    width: 210px;
    font-family: "Josefin Sans", sans-serif;
    font-weight: 300;
    font-size: 26px;
    line-height: 1.2;
    color: var(--ink-dark);
  }
  .contact {
    position: absolute;
    left: 282px;
    top: 92px;
    font-size: 11.5px;
    line-height: 1.3;
    color: var(--ink-soft);
  }
  .contact__name {
    font-size: 17px;
    font-weight: 700;
    color: var(--ink-dark);
  }
  .contact__role { margin-bottom: 8px; }
  .contact__company { font-weight: 700; color: var(--ink-dark); }
  .contact__address { margin-bottom: 12px; }

  /* Academy side */
  .card--academy {
    top: 480px;
    background: var(--card-dark);
    color: var(--ink-light);
    font-family: "Josefin Sans", sans-serif;
  }
  .academy-name {
    position: absolute;
    left: 0;
    right: 0;
    top: 86px;
    text-align: center;
    font-weight: 300;
    font-size: 24px;
    letter-spacing: 0.5px;
    color: var(--ink-light);
  }
  .academy-web {
    position: absolute;
    left: 0;
    right: 0;
    top: 215px;
    text-align: center;
    font-weight: 300;
    font-size: 22px;
    letter-spacing: 1.5px;
  }
</style>
</head>
<body>
<main class="canvas">

  <section class="card card--shop" aria-label="Shop side of business card">
    <p class="shop-name">Glinted Tavu Cosmetics</p>
    <div class="contact">
      <p class="contact__name">Dorotea Brankelis</p>
      <p class="contact__role">Director</p>
      <p class="contact__company">Glinted Tavu Cosmetics</p>
      <p class="contact__address">47 Tamsworth St. Kelverton Vic 3279</p>
      <p>M: 61-438217506</p>
      <p>E: dorotea@glowstudiocollege.com.au</p>
      <p>web: www.glintedtavu.com</p>
    </div>
  </section>

  <section class="card card--academy" aria-label="Academy side of business card">
    <p class="academy-name">Larkfield Makeup &amp; Hair Academy</p>
    <p class="academy-web">www.glowstudiocollege.com.au</p>
  </section>

</main>
</body>
</html>
```